In house, web site post, social media post, and email blast specials/promo flyer

We are looking to update our monthly specials flyer to be sent out via Bright Mailway as well as printed and handed out in office and social media and posted to our website. Please see attachments below for a sample of a previous flyer. We want it to look clean and not too busy. It should be professional looking as this is going to a higher end client that is paying cash for our services

Target Market(s)

Women and Men 35-55

Contact Information for Business Card

I am tired of our current business card and want a fresh updated look. We want something simple, clean, and modern looking.

Font styles to use
Sans Serif
Script

Colors
3377b5
34a7d8
85cae6
85abd2
cedeed
ecf7fb
eaf1f7

Requirements
Must have
• Clean lines, Sexy, appealing to the medical spa beauty industry. Our clients come to us to look and feel good.
• Content of actual specials:
• FIGHT FINE LINES AND WRINKLES-Purchase a minimum of 30 units of Lumivex and receive a complimentary Glycolic Acid Peel ($150 VALUE)
• THE SWEAT STOPS HERE-Permanently stop underarm sweat with DuraCalm treatments, starting at $1,950
• BRIGHTEN & TONE-IPL $ Beam Serenity package $3,500
• REDUCE FACE & LEG VEINS- 15% off packages
• VOLUMERA: CHEEKS & NL FOLDS-SECOND SYRINGE 25% OFF, THIRD SYRINGE $50 OFF
• BODY SCULPTING FOR ABDOMEN AND THIGHS-Blast unwanted fat with a trio of treatments! $4,799
Nice to have
• Here are some sample flyers of what we would like ours to look like
• https://www.kelomirskinspa.com/specials/
• https://brevanolaclinic.com/november-specials-2017/

```html
<!DOCTYPE html>
<html lang="en">
<head>
<meta charset="utf-8">
<title>Monthly Specials Flyer</title>
<link rel="stylesheet" href="https://fonts.googleapis.com/css2?family=Lato:wght@400;700;900&display=swap">
<style>
  :root {
    --teal: #2f8283;
    --teal-dark: #236c6e;
    --ink: #2b2b2b;
    --paper: #ffffff;
    --photo-green: #6f9a3a;
    --photo-dark: #3a2e38;
    --photo-amber: #e8a21c;
  }
  * { margin: 0; padding: 0; box-sizing: border-box; }
  html, body { width: 1200px; height: 848px; overflow: hidden; background: var(--paper); }
  body { font-family: "Lato", Arial, sans-serif; color: var(--ink); }
  .flyer { position: relative; width: 1200px; height: 848px; overflow: hidden; background: var(--paper); }
  .hero-photo {
    position: absolute; left: 0; top: 0; width: 1200px; height: 430px;
    background:
      radial-gradient(ellipse 300px 240px at 600px 170px, #d9b8a6 0%, rgba(217,184,166,0) 70%),
      linear-gradient(100deg, var(--photo-dark) 0%, var(--photo-green) 30%, #8a7a55 55%, var(--photo-amber) 85%, #f4c84a 100%);
  }
  .hero-wave { position: absolute; left: 0; top: 0; width: 1200px; height: 848px; }
  .brand {
    position: absolute; right: 24px; top: 196px;
    color: var(--teal-dark); font-size: 54px; font-weight: 400;
    letter-spacing: 4px; line-height: 1;
  }
  .headline {
    position: absolute; left: 60px; top: 350px; width: 1000px;
    color: var(--teal); font-weight: 900; font-size: 40px; line-height: 1.08; text-transform: uppercase;
  }
  .specials { position: absolute; top: 460px; width: 480px; }
  .specials--left { left: 60px; }
  .specials--right { left: 620px; }
  .special { margin-bottom: 16px; font-size: 17px; line-height: 1.25; }
  .special-title { color: var(--teal); font-weight: 900; text-transform: uppercase; }
  .footer-band { position: absolute; left: 0; top: 700px; width: 1200px; height: 148px; background: var(--teal); }
  .footer-tab {
    position: absolute; left: 340px; top: 690px; width: 460px; height: 70px;
    background: var(--paper); border-radius: 0 0 22px 22px;
    display: flex; align-items: center; justify-content: center;
  }
  .footer-url { color: var(--teal); font-weight: 900; font-size: 26px; }
  .footer-info {
    position: absolute; left: 0; top: 770px; width: 1200px; text-align: center;
    color: var(--paper); font-size: 14px; line-height: 1.45;
  }
  .footer-links { font-weight: 700; }
</style>
</head>
<body>
<main class="flyer">
  <div class="hero-photo" role="img" aria-label="Photo of a woman in a wide-brimmed dark hat against a soft green and golden garden background"></div>

  <svg class="hero-wave" viewBox="0 0 1200 848" aria-hidden="true">
    <path d="M0,300 C180,270 300,360 460,330 C620,300 700,200 860,330 C980,420 1100,400 1200,380 L1200,848 L0,848 Z" fill="#2f8283"/>
    <path d="M0,308 C180,278 300,368 460,338 C620,308 700,208 860,338 C980,428 1100,408 1200,388 L1200,848 L0,848 Z" fill="#ffffff"/>
  </svg>

  <div class="brand">LUMORA</div>

  <h1 class="headline">Please call to schedule your<br>appointment today 503.555.0142</h1>

  <section class="specials specials--left">
    <p class="special"><span class="special-title">Fight fine lines and wrinkles</span><br>Purchase a minimum of 30 units of Lumivex and receive a complimentary Glycolic Acid Peel ($150 VALUE)</p>
    <p class="special"><span class="special-title">Brighten &amp; Tone-IPL $</span><br>Beam Serenity package $3,500</p>
    <p class="special"><span class="special-title">VOLUMERA:</span> CHEEKS &amp; NL FOLDS-SECOND SYRINGE 25% OFF, THIRD SYRINGE $50 OFF</p>
  </section>

  <section class="specials specials--right">
    <p class="special"><span class="special-title">The sweat stops here</span><br>Permanently stop underarm sweat with DuraCalm treatments, starting at $1,950</p>
    <p class="special"><span class="special-title">Reduce face &amp; leg veins</span><br>15% off packages</p>
    <p class="special"><span class="special-title">Body sculpting for abdomen and thighs</span> Blast unwanted fat with a trio of treatments! $4,799</p>
  </section>

  <footer>
    <div class="footer-band"></div>
    <div class="footer-tab"><span class="footer-url">lumoraportland.com</span></div>
    <div class="footer-info">
      <p>2210 NW Alder Street, Suite 2, Portland, Oregon 97209 503.555.0142</p>
      <p>Visit lumoraportland.com for a more beautiful body, inside and out.</p>
      <p class="footer-links">https://www.kelomirskinspa.com/specials/ | https://brevanolaclinic.com/november-specials-2017/</p>
    </div>
  </footer>
</main>
</body>
</html>
```